Business Card Design

The image I attached was a quick thought to my design. I have triplets and was invisioning something with three figures with maybe the colors blue, pink and green. I would like it to look very chic and modern yet soothing/healing. I will take any fresh ideas as well.

Side 1: Contact Details
Side 2: Appointment section (mandatory)
Updates

Thank u all for your preliminary designs. I had sent the old design over and am looking for a bold fresh NEW LOOK  for CORE MOTION. I saw some really creative ideas in the gallery. If you have any other questions please feel free to email me at rtbwakes@quellmail.net.

Thanks

Please keep in mind that it is mandatory that on the back of the card is for appointments.

Thank you.

Reason: The two mandatory elements that need to be on the card is that her title needs to read as so:

Reason: The criteria is still not being met. Her title needs to read as so: Dr. Marisa Kettner, P.T., D.P.T. Doctor of Physical Therapy and The appointment info must go on the BACK of the card. Looking forward to some more great designs. Thanks.

Industry/Entity Type

Business

Contact Information for Business Card

Core Motion
Physical & Aquatic Therapy
Dr. Marisa Kettner, P.T., D.P.T.
Doctor of Physical Therapy

22-48 B Birchwick Lane
Elmbury, N.Y. 11592
(Located inside of the Summit gym in the Pinecrest shopping center)

Phone & Fax: (631) 555-0172
Mkettner4@harbornet.net

Requirements
Must have
• One the back I would like to do an appointment layout.

```html
<!DOCTYPE html>
<html lang="en">
<head>
<meta charset="utf-8">
<title>Core Motion – Business Card</title>
<link rel="stylesheet" href="https://fonts.googleapis.com/css2?family=Marcellus&family=Tenor+Sans&display=swap">
<style>
  :root {
    --page-bg: #d6d6d6;
    --card-top: #f3fbfc;
    --card-mid: #bfe6ea;
    --card-bottom: #3fb1bd;
    --white: #ffffff;
    --purple: #b04aa8;
    --green: #6cc04a;
    --ink: #111111;
    --grey: #6a6a6a;
    --field: #ffffff;
    --shadow: rgba(0,0,0,0.18);
  }
  * { margin: 0; padding: 0; box-sizing: border-box; }
  html, body { width: 1200px; height: 900px; overflow: hidden; }
  body {
    background: var(--page-bg);
    font-family: "Tenor Sans", "Helvetica Neue", Arial, sans-serif;
    color: var(--ink);
    position: relative;
  }
  .card {
    position: absolute;
    top: 295px;
    width: 540px;
    height: 310px;
    border-radius: 22px;
    overflow: hidden;
    background: linear-gradient(180deg, var(--card-top) 0%, var(--card-mid) 45%, var(--card-bottom) 100%);
    box-shadow: 0 10px 24px var(--shadow);
  }
  .card-front { left: 40px; }
  .card-back { left: 620px; }

  .front-shape { position: absolute; inset: 0; }
  .brand-mark {
    position: absolute;
    left: 14px; top: 120px;
    width: 150px;
    display: flex; align-items: center; gap: 8px;
    color: var(--purple);
    font-size: 17px;
  }
  .brand-mark .dot {
    width: 16px; height: 16px; border-radius: 50%;
    background: var(--purple); flex: none;
  }
  .front-text { position: absolute; left: 212px; top: 28px; right: 14px; }
  .brand-name {
    font-family: "Marcellus", Georgia, serif;
    font-size: 34px; line-height: 1; color: var(--purple);
    letter-spacing: 0.5px; white-space: nowrap;
  }
  .brand-tagline { font-size: 17px; color: var(--green); margin-top: 4px; white-space: nowrap; }
  .person { margin-top: 26px; padding-left: 18px; }
  .person-name { font-size: 16px; }
  .person-title { font-size: 12.5px; color: var(--grey); margin-top: 2px; }
  .contact { margin-top: 26px; padding-left: 0; font-size: 14.5px; line-height: 1.3; }
  .contact .email { padding-left: 14px; }
  .contact .note { font-size: 9.5px; line-height: 1.3; margin-top: 1px; white-space: nowrap; margin-left: -40px; }

  .appt-title { position: absolute; top: 36px; left: 0; right: 0; text-align: center; font-size: 20px; }
  .days { position: absolute; top: 88px; left: 82px; right: 18px; display: flex; justify-content: space-between; }
  .day { display: flex; flex-direction: column; align-items: center; gap: 6px; }
  .day-label { font-size: 15px; }
  .day-box { width: 46px; height: 30px; background: var(--field); }
  .date-time {
    position: absolute; top: 162px; left: 26px; right: 18px;
    display: flex; align-items: center; gap: 8px; font-size: 15px;
  }
  .date-time .field { height: 36px; background: var(--field); }
  .date-time .date-field { width: 178px; }
  .date-time .time-field { flex: 1; }
  .pool { position: absolute; left: 30px; bottom: 34px; font-size: 14px; line-height: 1.4; }
</style>
</head>
<body>

<section class="card card-front" aria-label="Business card front">
  <svg class="front-shape" viewBox="0 0 540 310" width="540" height="310" aria-hidden="true">
    <path d="M0 0 H192 C214 90 200 220 122 310 H0 Z" fill="var(--white)"/>
    <path d="M138 0 H194 C214 70 206 160 178 220 C192 140 182 60 138 0 Z" fill="var(--purple)"/>
  </svg>
  <div class="brand-mark"><span class="dot"></span><span>Core Motion</span></div>
  <div class="front-text">
    <h1 class="brand-name">CORE MOTION</h1>
    <p class="brand-tagline">Physical &amp; Aquatic Therapy</p>
    <div class="person">
      <p class="person-name">Dr. Marisa Kettner, P.T., D.P.T.</p>
      <p class="person-title">Doctor of Physical Therapy</p>
    </div>
    <div class="contact">
      <p>Phone &amp; Fax: (631) 555-0172</p>
      <p class="email">Mkettner4@harbornet.net</p>
      <p>22-48 B Birchwick Lane Elmbury,</p>
      <p>N.Y. 11592</p>
      <p class="note">(Located inside of the Summit gym in the Pinecrest shopping center)</p>
    </div>
  </div>
</section>

<section class="card card-back" aria-label="Business card back">
  <h2 class="appt-title">Appointment</h2>
  <div class="days">
    <div class="day"><span class="day-label">Mon</span><span class="day-box"></span></div>
    <div class="day"><span class="day-label">Tue</span><span class="day-box"></span></div>
    <div class="day"><span class="day-label">Wed</span><span class="day-box"></span></div>
    <div class="day"><span class="day-label">Thu</span><span class="day-box"></span></div>
    <div class="day"><span class="day-label">Fri</span><span class="day-box"></span></div>
    <div class="day"><span class="day-label">Sat</span><span class="day-box"></span></div>
  </div>
  <div class="date-time">
    <span>Date</span><span class="field date-field"></span>
    <span>Time</span><span class="field time-field"></span>
  </div>
  <div class="pool">
    <p>Pool location- Summit gym in Larkdale</p>
    <p>318 Rt. 40B</p>
    <p>Larkdale, N.Y. 11604</p>
  </div>
</section>

</body>
</html>
```